Verpackungsdesign für vegane Spielknete
Zielgruppe
BOLMU® ist deutscher Hersteller von veganer Spielknete für Kinder ab 1 Jahr.
Zielgruppe: Moderne Familien, die Wert auf hochwertige und schöne Spielsachen für ihre Kinder Wert legen. Instagram Mamas. Gewichtung: 75% W / 25% M
Aufgabenstellung
Situation: Wir haben aktuell eine braune einfache Kartonage mit einem XXL Siegel ummantelt.
Ziel: Neues Packaging mit vollflächigen Druck. Es soll sich nicht so weit von unserem aktuellen Design entfernen, darf aber gerne noch moderner und stylischer sein. Schriften lieben wir gerne weiß auf braunen Karton.
Neue Kartonage: Außen Kraftpapier Braun // Innen Weiß Beschichtet Glatt // Highlight: Ein Monstera Blatt legt sich über die BAGs.
Hinweis: Wir haben 4 verschiedne Boxen zu designen. Bitte vorerst auf das 8er BAG SET fokussieren. Das aktuelle Siegel findest du anbei. Die Warnhinweise etc. müssen final dann alle übernommen werden. Also alles was du auf der Rückseite des Siegels findest muss auch auf die neue Kartonage. https://www.bolmu-beispiel.de/collections/bolmu®-set-bags/products/bolmu®-8er-set-bags
Info: Siehe unser CI Briefing.

```html
<!DOCTYPE html>
<html lang="de">
<head>
<meta charset="utf-8">
<title>BOLMU® – Verpackung 8er BAG SET</title>
<link href="https://fonts.googleapis.com/css2?family=Montserrat:wght@400;500;600;700&family=Kaushan+Script&display=swap" rel="stylesheet">
<style>
:root{
  --bg-top:#e3ded4;
  --bg-mid:#ebe6df;
  --bg-low:#efebe4;
  --box-green:#3f8654;
  --leaf:#4f7f50;
  --leaf-light:#9fc79c;
  --kraft:#c9a57a;
  --kraft-light:#d8b78e;
  --pink:#e3207a;
  --teal:#2a9a8e;
  --teal-light:#6ab9b0;
  --ink:#262626;
  --paper:#ffffff;
  --fold:#b9d6c1;
}
*{margin:0;padding:0;box-sizing:border-box}
html,body{width:1200px;height:2891px;overflow:hidden}
body{position:relative;font-family:"Montserrat",Arial,sans-serif;color:var(--ink);background:var(--bg-top)}
.section{position:absolute;left:0;width:1200px}
.section--dielines{top:0;height:1105px;background:var(--bg-top)}
.section--front{top:1105px;height:895px;background:var(--bg-mid)}
.section--side{top:2000px;height:891px;background:var(--bg-low)}
.abs{position:absolute}
.label{position:absolute;top:58px;font-size:17px;font-weight:500;transform:translateX(-50%)}

/* outer dieline */
.flap-top{left:147px;top:140px;width:321px;height:232px;background:var(--box-green);border-radius:14px 14px 0 0}
.flap-top .fold{position:absolute;left:0;right:0;top:113px;border-top:1px dashed rgba(255,255,255,.25)}
.flap-top .leaf-ghost{position:absolute;left:90px;top:50px;width:140px;height:130px;border-radius:50% 50% 45% 55%;border:2px solid rgba(20,70,40,.35)}
.band{left:40px;top:370px;width:535px;height:332px;background:var(--box-green)}
.band .fold-v{position:absolute;top:0;bottom:0;border-left:1px dashed rgba(255,255,255,.25)}
.band .fold-h{position:absolute;left:0;right:0;border-top:1px dashed rgba(255,255,255,.25)}
.band .url{position:absolute;left:0;right:0;text-align:center;font-family:"Kaushan Script",cursive;color:#fff;font-size:18px;line-height:22px}
.band .tagline{position:absolute;left:0;right:0;text-align:center;color:rgba(255,255,255,.7);font-size:5px;letter-spacing:.5px}
.flipped{transform:rotate(180deg)}
.side-strip{position:absolute;width:26px;display:flex;flex-direction:column;align-items:center;gap:5px}
.age-badge{width:26px;height:26px;border-radius:50%;background:var(--teal);color:#fff;font-weight:700;font-size:7px;line-height:7px;display:flex;flex-direction:column;align-items:center;justify-content:center;text-align:center}
.dot{width:8px;height:8px;border-radius:50%}
.c1{background:#d8262f}.c2{background:#e3207a}.c3{background:#f39a1d}.c4{background:#f4d21a}.c5{background:#3aa441}.c6{background:#19a3c8}.c7{background:#2b55a5}.c8{background:#3c2f86}

.back-panel{left:138px;top:418px;width:339px;height:237px;background:var(--paper);padding:12px 16px;font-size:4.6px;line-height:1.35}
.back-panel .cols{display:flex;gap:14px}
.back-panel .col{flex:1;display:flex;flex-direction:column;gap:3px}
.back-item{display:flex;gap:4px;align-items:center}
.back-item i{flex:none;width:8px;height:8px;border-radius:50%;background:var(--pink)}
.back-item b{font-weight:700}
.warnings{margin-top:8px;display:flex;flex-direction:column;gap:2px}
.back-foot{position:absolute;left:16px;right:16px;bottom:12px;display:flex;justify-content:space-between;align-items:flex-end;font-size:4.5px;text-align:center}
.back-foot .content b{font-size:8px;font-weight:600;display:block}
.back-foot .dots{display:flex;gap:2px;margin:2px 0}
.back-foot .dots .dot{width:6px;height:6px}
.cert-row{display:flex;gap:3px}
.cert-row span{width:10px;height:8px;background:#333;border-radius:1px}
.ce{font-size:9px;font-weight:600;margin-top:4px}

.front-small{left:99px;top:702px;width:420px;height:286px;border-radius:0 0 14px 14px;overflow:hidden}
.leaf-frame{position:absolute;inset:0;background:radial-gradient(ellipse 48% 44% at 50% 56%,var(--paper) 60%,#cfe0cc 78%,var(--leaf) 100%)}
.leaf-frame.kraft{background:radial-gradient(ellipse 48% 44% at 50% 55%,var(--kraft-light) 0%,var(--kraft) 62%,#7b9a6a 82%,#2f5b3a 100%)}

/* front content, designed at 574 × 404 */
.front-content{position:absolute;left:0;top:0;width:574px;height:404px;transform-origin:0 0}
.front-content .age-badge{position:absolute;left:102px;top:158px;width:44px;height:44px;font-size:13px;line-height:12px}
.brand{position:absolute;left:168px;top:146px;font-weight:600;font-size:62px;letter-spacing:1px;color:var(--ink);line-height:1;white-space:nowrap}
.descriptor{position:absolute;left:172px;top:216px;font-weight:500;font-size:17px;letter-spacing:2px;color:var(--ink);text-transform:uppercase}
.colours{position:absolute;left:140px;top:270px;display:flex;align-items:center;gap:4px}
.colours em{font-family:"Kaushan Script",cursive;font-style:normal;font-size:13px;margin-right:6px}
.colours .dot{width:13px;height:13px}
.filled{position:absolute;left:334px;top:258px;font-family:"Kaushan Script",cursive;font-size:23px;color:var(--ink)}
.filled span{color:var(--pink)}
.little{position:absolute;left:388px;top:290px;font-size:9px}
.features{position:absolute;left:141px;top:308px;display:flex;gap:19px}
.feature{width:29px;display:flex;flex-direction:column;align-items:center;gap:3px;font-size:4.5px;font-weight:700;text-align:center;line-height:1.2}
.feature i{width:29px;height:29px;border-radius:50%;background:var(--pink);box-shadow:inset 0 0 0 3px var(--pink),inset 0 0 0 4px #fff}

/* inner dieline */
.inner-top{left:696px;top:140px;width:419px;height:287px;border-radius:14px 14px 0 0;overflow:hidden}
.inner-top .text{position:absolute;left:0;right:0;text-align:center}
.hello{font-family:"Kaushan Script",cursive;color:var(--pink);font-size:40px;letter-spacing:1px;line-height:48px}
.hashtags{font-family:"Kaushan Script",cursive;color:var(--teal-light);font-size:17px;line-height:22px}
.thanks{font-family:"Kaushan Script",cursive;color:var(--pink);font-size:24px;line-height:30px}
.social{display:flex;align-items:center;gap:6px;font-size:7px;margin-top:5px}
.social i{width:9px;height:9px;border-radius:50%;border:1.3px solid #444}
.inner-mid{left:638px;top:430px;width:533px;height:328px;background:var(--paper);border:1px solid var(--fold)}
.inner-mid .fold-v{position:absolute;top:0;bottom:0;border-left:1px dashed var(--fold)}
.inner-mid .fold-h{position:absolute;left:0;right:0;border-top:1px dashed var(--fold)}
.colour-wheel{position:absolute;left:162px;top:64px;width:196px;height:196px;border-radius:50%;background:radial-gradient(circle,#f1e9df 0 46%,transparent 47%),conic-gradient(#e3207a,#a33b93,#19a3c8,#1f7f8a,#3aa441,#6b4a2e,#f3ede2,#f4d21a,#f39a1d,#d8262f,#e3207a)}
.inner-bottom{left:744px;top:758px;width:322px;height:230px;border:1px solid var(--fold);border-radius:0 0 14px 14px;overflow:hidden;background:var(--paper)}
.inner-bottom .ground{position:absolute;left:0;right:0;bottom:0;height:110px;background:linear-gradient(to top,#6c9a68,rgba(255,255,255,0))}
.monstera{position:absolute;left:95px;top:30px;width:132px;height:110px;border-radius:55% 45% 50% 50%;background:var(--leaf-light)}
.tag-pink{position:absolute;font-family:"Kaushan Script",cursive;color:var(--pink);font-size:17px;line-height:22px}

/* side panel */
.side-panel{left:300px;top:330px;width:600px;height:170px;background:var(--box-green);border-radius:4px;box-shadow:0 20px 40px rgba(0,0,0,.08)}
.side-panel .age-badge{position:absolute;left:40px;top:56px;width:56px;height:56px;font-size:15px;line-height:14px}
.side-panel .dots{position:absolute;left:220px;top:77px;display:flex;gap:12px}
.side-panel .dot{width:16px;height:16px}
</style>
</head>
<body>

<section class="section section--dielines">
  <div class="label" style="left:302px">aussen</div>
  <div class="label" style="left:903px">innen</div>

  <div class="abs flap-top">
    <div class="fold"></div>
    <div class="leaf-ghost" role="img" aria-label="Geprägtes Monstera-Blatt als Linienzeichnung"></div>
  </div>

  <div class="abs band">
    <div class="fold-v" style="left:98px"></div>
    <div class="fold-v" style="left:437px"></div>
    <div class="fold-h" style="top:48px"></div>
    <div class="fold-h" style="top:285px"></div>
    <div class="tagline" style="top:10px">DEIN WEG ZUR KNETFREUDE</div>
    <div class="url" style="top:20px">www.bolmu-beispiel.de</div>
    <div class="url flipped" style="top:290px">www.bolmu-beispiel.de</div>
    <div class="tagline flipped" style="top:318px">DEIN WEG ZUR KNETFREUDE</div>

    <div class="side-strip" style="left:61px;top:62px">
      <div class="age-badge">+1<br>AGE</div>
      <div style="height:40px"></div>
      <span class="dot c1"></span><span class="dot c2"></span><span class="dot c3"></span><span class="dot c4"></span>
      <span style="height:4px"></span>
      <span class="dot c5"></span><span class="dot c6"></span><span class="dot c7"></span><span class="dot c8"></span>
    </div>
    <div class="side-strip" style="left:448px;top:62px">
      <div class="age-badge">+1<br>AGE</div>
      <div style="height:40px"></div>
      <span class="dot c1"></span><span class="dot c2"></span><span class="dot c3"></span><span class="dot c4"></span>
      <span style="height:4px"></span>
      <span class="dot c5"></span><span class="dot c6"></span><span class="dot c7"></span><span class="dot c8"></span>
    </div>
  </div>

  <div class="abs back-panel">
    <div class="cols">
      <div class="col">
        <div class="back-item"><i></i><span><b>Geeignet für Kinder ab 1 Jahr.</b> Für sicheren Knetspaß.</span></div>
        <div class="back-item"><i></i><span><b>UMWELT:</b> Die Knetmasse ist kompostierbar.</span></div>
        <div class="back-item"><i></i><span><b>EXTRA KLAR:</b> Wir achten auf hochwertige Zutaten.</span></div>
        <div class="back-item"><i></i><span><b>Angenehme Haptik:</b> Perfekt für kleine Hände.</span></div>
      </div>
      <div class="col">
        <div class="back-item"><i></i><span><b>GESUND:</b> Ohne Gluten, ohne Nüsse.</span></div>
        <div class="back-item"><i></i><span><b>VEGAN:</b> Ohne tierische Zutaten.</span></div>
        <div class="back-item"><i></i><span><b>Herstellung in Bayern:</b> Regionale Fertigung.</span></div>
      </div>
    </div>
    <div class="warnings">
      <p><b>DE ACHTUNG:</b> Nur unter Aufsicht Erwachsener verwenden. Luftdicht lagern.</p>
      <p><b>GB ATTENTION:</b> Use only under adult supervision. Store airtight.</p>
      <p><b>ES ATENCIÓN:</b> Usar solo bajo supervisión de un adulto.</p>
      <p><b>IT ATTENZIONE:</b> Usare solo sotto la supervisione di un adulto.</p>
      <p><b>FR ATTENTION:</b> À utiliser sous la surveillance d'un adulte.</p>
      <p><b>NL LET OP:</b> Alleen gebruiken onder toezicht van een volwassene.</p>
    </div>
    <div class="back-foot">
      <div class="content">
        Inhalt<b>8 x 50 g</b>
        <div class="dots"><span class="dot c1"></span><span class="dot c2"></span><span class="dot c3"></span><span class="dot c4"></span><span class="dot c5"></span><span class="dot c6"></span><span class="dot c7"></span><span class="dot c8"></span></div>
        Spielknete / play dough<br>Charge Nr.: 05-0000<br>Artikelnummer BM_DP8_50
      </div>
      <div>
        BOLMU®<br>Musterweg 12<br>DE-97000 Musterstadt<br>hallo@bolmu-beispiel.de
        <div style="margin-top:4px"><b>DE</b> Hauptbestandteile: Wasser, Mehl, Salz</div>
        <div><b>GB</b> Modelling clay: water, flour, salt</div>
        <div class="ce">CE</div>
      </div>
      <div class="cert-row"><span></span><span></span><span></span><span></span></div>
    </div>
  </div>

  <div class="abs front-small">
    <div class="leaf-frame" role="img" aria-label="Aquarell-Monstera- und Palmblätter rahmen den Namen ein"></div>
    <div class="front-content" style="transform:translate(-20px,-20px) scale(0.73)">
      <div class="age-badge">+1<br>AGE</div>
      <div class="brand">BOLMU®</div>
      <div class="descriptor">vegane Spielknete</div>
      <div class="colours"><em>Farben</em><span class="dot c1"></span><span class="dot c2"></span><span class="dot c3"></span><span class="dot c4"></span><span class="dot c5"></span><span class="dot c6"></span><span class="dot c7"></span><span class="dot c8"></span></div>
      <div class="filled">#filled with <span>love</span></div>
      <div class="little">&amp; a little dough</div>
      <div class="features">
        <div class="feature"><i></i>MADE IN GERMANY</div>
        <div class="feature"><i></i>AB 1 JAHR</div>
        <div class="feature"><i></i>100% VEGAN</div>
        <div class="feature"><i></i>ANGENEHME GRIFFE</div>
        <div class="feature"><i></i>KNETE IN BIOFORM</div>
        <div class="feature"><i></i>120% DESIGN</div>
        <div class="feature"><i></i>OHNE ALAUN</div>
      </div>
    </div>
  </div>

  <div class="abs inner-top">
    <div class="leaf-frame" role="img" aria-label="Aquarell-Monstera- und Palmblätter an den Rändern"></div>
    <div class="text" style="top:60px;font-size:16px;font-weight:600">BOLMU®</div>
    <div class="text hello" style="top:80px">HALLO</div>
    <div class="text" style="top:134px;font-size:8.5px;line-height:1.3">Schön dich zu sehen.<br>Ich bin eine BOLMU® BOX. Gemeinsam werden wir<br>wunderschöne FAMILIEN-MOMENTE erschaffen.</div>
    <div class="text" style="top:172px;font-size:5px;line-height:1.4">Nice to see you.<br>I am a BOLMU® BOX. Together we will create beautiful FAMILY MOMENTS.</div>
    <div class="text hashtags" style="top:190px">#knetspass #familienzeit</div>
    <div class="abs" style="left:70px;top:222px;width:120px;font-size:8.5px;text-align:center">Die BOLMU® CREW sagt
      <div class="thanks">DANKE</div>
    </div>
    <div class="abs" style="left:218px;top:222px;font-size:8.5px">Für Knetideen folge uns auf:
      <div class="social" style="margin-left:12px"><i></i>@bolmu_knete</div>
      <div class="social" style="margin-left:12px"><i></i>@bolmu</div>
    </div>
  </div>

  <div class="abs inner-mid">
    <div class="fold-v" style="left:20px"></div>
    <div class="fold-v" style="left:100px"></div>
    <div class="fold-v" style="left:432px"></div>
    <div class="fold-v" style="left:512px"></div>
    <div class="fold-h" style="top:40px"></div>
    <div class="fold-h" style="top:288px"></div>
    <div class="colour-wheel" role="img" aria-label="Kreis aus bunten Knetrollen um ein Foto eines Kindes mit Knetbeuteln"></div>
  </div>

  <div class="abs inner-bottom">
    <div class="ground" role="img" aria-label="Aquarell-Palmblätter am unteren Rand"></div>
    <div class="monstera" role="img" aria-label="Großes hellgrünes Monstera-Blatt"></div>
    <div class="tag-pink" style="left:10px;top:122px">#knetspass</div>
    <div class="tag-pink" style="left:212px;top:122px">#familienzeit</div>
    <div class="abs" style="left:0;right:0;top:152px;text-align:center;font-size:34px;font-weight:600;color:var(--ink);line-height:40px">BOLMU®</div>
    <div class="abs" style="left:0;right:0;top:194px;text-align:center;font-size:10px;font-weight:500;letter-spacing:2px;color:var(--ink);text-transform:uppercase">vegane Spielknete</div>
  </div>
</section>

<section class="section section--front">
  <div class="abs" style="left:313px;top:248px;width:574px;height:404px;overflow:hidden;box-shadow:0 30px 60px rgba(0,0,0,.08)">
    <div class="leaf-frame kraft" role="img" aria-label="Aquarell-Monstera- und Palmblätter auf braunem Kraftkarton"></div>
    <div class="front-content">
      <div class="age-badge">+1<br>AGE</div>
      <div class="brand">BOLMU®</div>
      <div class="descriptor">vegane Spielknete</div>
      <div class="colours"><em>Farben</em><span class="dot c1"></span><span class="dot c2"></span><span class="dot c3"></span><span class="dot c4"></span><span class="dot c5"></span><span class="dot c6"></span><span class="dot c7"></span><span class="dot c8"></span></div>
      <div class="filled">#filled with <span>love</span></div>
      <div class="little">&amp; a little dough</div>
      <div class="features">
        <div class="feature"><i></i>MADE IN GERMANY</div>
        <div class="feature"><i></i>AB 1 JAHR</div>
        <div class="feature"><i></i>100% VEGAN</div>
        <div class="feature"><i></i>ANGENEHME GRIFFE</div>
        <div class="feature"><i></i>KNETE IN BIOFORM</div>
        <div class="feature"><i></i>120% DESIGN</div>
        <div class="feature"><i></i>OHNE ALAUN</div>
      </div>
    </div>
  </div>
</section>

<section class="section section--side">
  <div class="abs side-panel">
    <div class="age-badge">+1<br>AGE</div>
    <div class="dots"><span class="dot c1"></span><span class="dot c2"></span><span class="dot c3"></span><span class="dot c4"></span><span class="dot c5"></span><span class="dot c6"></span><span class="dot c7"></span><span class="dot c8"></span></div>
  </div>
</section>

</body>
</html>
```